Looking for an amazing business card for a thriving DJ business

We need a business card design for a DJ company based in South Florida. The DJ company specializes in weddings, parties, bar mitzvahs, corporate events, proms, and reunions. We are looking for a modern, simple business card design. The card should state DJ Marlow K.
Updates

The name on the card should be DJ Marlow K

Industry/Entity Type

Entertainment Industry

Contact Information for Business Card

DJ Marlow K
512.447.2086
atxdjmarlowk@quellmail.com
https://www.facebook.com/DjMarlowK/
https://www.instagram.com/djmarlow.k/
www.djmarlowk.net

Font styles to use
Serif
Sans Serif

Requirements
Must have
• My business card has to be awesome.
Should not have
• The card has to have personality.

```html
<!DOCTYPE html>
<html lang="en">
<head>
<meta charset="utf-8">
<title>DJ Marlow K — Business Card</title>
<link rel="stylesheet" href="https://fonts.googleapis.com/css2?family=Marcellus&family=Poppins:ital,wght@0,300;0,400;1,400&display=swap">
<style>
  :root {
    --canvas-bg: #8a8a8a;
    --card-black: #0b0b0c;
    --card-charcoal: #1c1c1e;
    --gold-light: #e2c489;
    --gold: #c9a464;
    --gold-deep: #9c763e;
    --silver-light: #d9d6d2;
    --silver: #8e8a86;
    --ink-dark: #1a1712;
    --text-light: #e9e7e4;
    --icon-white: #f4f2ef;
    --wave-red: #4a0c0c;
  }
  * { box-sizing: border-box; margin: 0; padding: 0; }
  html, body { width: 1200px; height: 800px; overflow: hidden; }
  body {
    background: var(--canvas-bg);
    display: flex;
    align-items: center;
    justify-content: center;
    gap: 40px;
    font-family: "Poppins", sans-serif;
  }
  .card {
    position: relative;
    width: 560px;
    height: 320px;
    overflow: hidden;
    background: var(--card-black);
  }

  /* Contact side */
  .card-contact .card-art { position: absolute; inset: 0; width: 100%; height: 100%; }
  .brand-header {
    position: absolute;
    top: 16px;
    left: 22px;
    display: flex;
    align-items: flex-start;
    gap: 14px;
  }
  .brand-circle {
    width: 56px; height: 56px;
    border-radius: 50%;
    background: var(--icon-white);
    flex: none;
  }
  .brand-name {
    font-family: "Marcellus", serif;
    font-size: 24px;
    font-weight: 400;
    color: var(--ink-dark);
    line-height: 1.1;
    margin-top: 4px;
  }
  .brand-tagline {
    font-family: "Poppins", sans-serif;
    font-style: italic;
    font-size: 8.2px;
    color: var(--ink-dark);
    line-height: 1.45;
    margin-top: 4px;
    max-width: 300px;
  }
  .contact-list {
    position: absolute;
    left: 22px;
    top: 142px;
    list-style: none;
    display: flex;
    flex-direction: column;
    gap: 6px;
  }
  .contact-item {
    display: flex;
    align-items: center;
    gap: 12px;
    font-size: 13px;
    font-weight: 300;
    color: var(--text-light);
    letter-spacing: 0.2px;
    line-height: 1.35;
  }
  .contact-icon {
    width: 24px; height: 24px;
    border-radius: 50%;
    background: var(--icon-white);
    flex: none;
    display: flex;
    align-items: center;
    justify-content: center;
  }
  .contact-icon.is-gold { background: var(--gold); }
  .contact-icon svg { width: 14px; height: 14px; }

  /* Brand side */
  .card-brand {
    background: radial-gradient(ellipse at 50% 45%, var(--card-charcoal) 0%, var(--card-black) 70%);
  }
  .sound-band {
    position: absolute;
    left: 0; right: 0;
    top: 128px;
    height: 80px;
    background: linear-gradient(90deg, transparent 0%, var(--wave-red) 20%, transparent 45%, var(--wave-red) 70%, transparent 100%);
    opacity: 0.55;
  }
  .brand-lockup {
    position: absolute;
    inset: 0;
    display: flex;
    flex-direction: column;
    align-items: center;
    justify-content: center;
  }
  .lockup-row { display: flex; align-items: center; gap: 14px; }
  .lockup-circle {
    width: 40px; height: 40px;
    border-radius: 50%;
    background: var(--gold);
  }
  .lockup-name {
    font-family: "Marcellus", serif;
    font-size: 38px;
    font-weight: 400;
    color: var(--gold);
    line-height: 1;
  }
  .lockup-industry {
    margin-top: 10px;
    font-size: 14px;
    letter-spacing: 3px;
    color: var(--text-light);
  }
</style>
</head>
<body>

  <section class="card card-contact" aria-label="Business card, contact side">
    <svg class="card-art" viewBox="0 0 560 320" preserveAspectRatio="none" aria-hidden="true">
      <defs>
        <linearGradient id="goldFill" x1="0" y1="0" x2="1" y2="0.3">
          <stop offset="0" stop-color="#d9bb80"/>
          <stop offset="0.5" stop-color="#c9a464"/>
          <stop offset="1" stop-color="#b68e4f"/>
        </linearGradient>
        <linearGradient id="silverFill" x1="0" y1="0" x2="1" y2="0">
          <stop offset="0" stop-color="#5a5652"/>
          <stop offset="0.5" stop-color="#d9d6d2"/>
          <stop offset="1" stop-color="#8e8a86"/>
        </linearGradient>
        <linearGradient id="goldEdge" x1="0" y1="0" x2="1" y2="0">
          <stop offset="0" stop-color="#9c763e"/>
          <stop offset="0.4" stop-color="#e2c489"/>
          <stop offset="1" stop-color="#9c763e"/>
        </linearGradient>
        <linearGradient id="darkBody" x1="0" y1="0" x2="0" y2="1">
          <stop offset="0" stop-color="#1c1c1e"/>
          <stop offset="1" stop-color="#070707"/>
        </linearGradient>
      </defs>
      <rect width="560" height="320" fill="url(#darkBody)"/>
      <path d="M0 0 H560 V112 C470 88 380 86 300 104 C200 126 90 136 0 134 Z" fill="url(#goldFill)"/>
      <path d="M0 122 C90 128 200 120 300 100 C380 86 470 84 560 104 V114 C470 96 380 96 300 110 C200 132 90 142 0 140 Z" fill="url(#goldEdge)"/>
      <path d="M210 116 C300 88 420 76 560 108 V122 C430 92 310 96 210 116 Z" fill="url(#silverFill)"/>
    </svg>

    <header class="brand-header">
      <span class="brand-circle" aria-hidden="true"></span>
      <div>
        <h1 class="brand-name">DJ Marlow K</h1>
        <p class="brand-tagline">The DJ company specializes in weddings, parties, bar mitzvahs,<br>corporate events, proms, and reunions.</p>
      </div>
    </header>

    <ul class="contact-list">
      <li class="contact-item">
        <span class="contact-icon is-gold" aria-hidden="true">
          <svg viewBox="0 0 24 24"><path d="M6.6 10.8a15 15 0 0 0 6.6 6.6l2.2-2.2c.3-.3.7-.4 1-.2 1.1.4 2.3.6 3.6.6.6 0 1 .4 1 1V20c0 .6-.4 1-1 1A17 17 0 0 1 3 4c0-.6.4-1 1-1h3.5c.6 0 1 .4 1 1 0 1.3.2 2.5.6 3.6.1.3 0 .7-.2 1z" fill="#1a1712"/></svg>
        </span>
        (512) 447-2086
      </li>
      <li class="contact-item">
        <span class="contact-icon" aria-hidden="true">
          <svg viewBox="0 0 24 24"><rect x="3" y="6" width="18" height="12" rx="1.5" fill="#1a1712"/><path d="M3.5 7 L12 13 L20.5 7" stroke="#f4f2ef" stroke-width="1.5" fill="none"/></svg>
        </span>
        <span>atxdjmarlowk@brightpost.com<br>atxdjmarlowk@quellmail.com</span>
      </li>
      <li class="contact-item">
        <span class="contact-icon" aria-hidden="true">
          <svg viewBox="0 0 24 24" fill="none" stroke="#1a1712" stroke-width="1.6"><circle cx="12" cy="12" r="8.5"/><ellipse cx="12" cy="12" rx="3.8" ry="8.5"/><path d="M3.5 12 H20.5 M5 7.5 H19 M5 16.5 H19"/></svg>
        </span>
        www.djmarlowk.net
      </li>
      <li class="contact-item">
        <span class="contact-icon" aria-hidden="true"></span>
        www.fanpage.social/DjMarlowK/
      </li>
      <li class="contact-item">
        <span class="contact-icon" aria-hidden="true"></span>
        www.snapgrid.social/djmarlow.k/
      </li>
    </ul>
  </section>

  <section class="card card-brand" aria-label="Business card, brand side">
    <div class="sound-band" role="img" aria-label="Faint dark red sound waveform running across the card"></div>
    <div class="brand-lockup">
      <div class="lockup-row">
        <span class="lockup-circle" aria-hidden="true"></span>
        <h2 class="lockup-name">DJ Marlow K</h2>
      </div>
      <p class="lockup-industry">Entertainment Industry</p>
    </div>
  </section>

</body>
</html>
```